Brand-new Pediatric Dental Practice needs a website

We are a brand-new dental practice that will specialize in treating children. We want a gorgeous and easily navigable dental practice website that would make a good first impression to potential patients and their parents. It should be modern, SEO-friendly, mobile responsive, and optimized to win new patients.

Target Market(s)

Parents

Industry/Entity Type

Healthcare/Dentistry

Coding

Coded - Design and coding required

Number of Pages Required

4 page

Requirements
Must have
• Use the Wix website building platform. 4 pages: home, meet our dentists, services, contact us
Nice to have
• has a link to our facebook, instagram

```html
<!DOCTYPE html>
<html lang="en">
<head>
<meta charset="utf-8">
<title>Maple Grove Pediatric Dentistry</title>
<link href="https://fonts.googleapis.com/css2?family=Lexend:wght@300;400;500&display=swap" rel="stylesheet">
<style>
:root{
  --green:#4cb061;
  --green-dark:#2f9a46;
  --green-bar:#37a44f;
  --green-soft:#d9efdc;
  --ink:#222;
  --text:#555;
  --dark:#2e3032;
  --footer:#343537;
  --light:#f1f3f6;
  --field:#f2f3f5;
  --white:#fff;
}
*{margin:0;padding:0;box-sizing:border-box}
html,body{width:1200px;height:3955px;overflow:hidden}
body{font-family:'Lexend',sans-serif;color:var(--ink);background:var(--white);position:relative}
.abs{position:absolute}
a{color:inherit;text-decoration:none}
.photo{position:absolute}
.badge{position:absolute;font-size:13px;font-weight:400;padding:0 15px;height:41px;line-height:41px;text-transform:uppercase;border-radius:3px}
.badge.soft{background:var(--green-soft);color:var(--green-dark)}
.badge.white{background:var(--white);color:var(--green-dark)}
.btn{position:absolute;background:var(--green-dark);color:var(--white);font-size:13px;text-transform:uppercase;border-radius:3px;display:flex;align-items:center;justify-content:center}
.h2{position:absolute;font-weight:400;font-size:43px;line-height:1.17}
.more{position:absolute;color:var(--green-dark);font-size:13px;text-transform:uppercase}

/* header */
.logo-box{left:0;top:0;width:174px;height:105px;background:var(--dark);color:var(--white);text-align:center}
.logo-box .mark{width:34px;height:34px;border-radius:50%;background:var(--green);margin:14px auto 6px}
.logo-box .name{font-size:20px;line-height:1}
.logo-box .sub{font-size:7px;letter-spacing:2px;text-transform:uppercase;margin-top:3px}
.topbar{left:174px;top:0;width:1026px;height:48px;background:var(--green-bar);color:var(--white);font-size:13px}
.topbar .item{position:absolute;top:0;height:48px;display:flex;align-items:center;gap:10px}
.topbar .sep{position:absolute;top:0;width:1px;height:48px;background:rgba(255,255,255,.25)}
.social-dot{width:10px;height:10px;border-radius:50%;background:var(--white)}
.navrow{left:174px;top:48px;width:1026px;height:57px;border-bottom:1px solid #e5e5e5;font-size:13px}
.navrow .link{position:absolute;top:21px}
.menu-box{left:1140px;top:48px;width:60px;height:57px;background:var(--green);display:flex;flex-direction:column;align-items:center;justify-content:center;gap:4px}
.menu-box span{width:24px;height:2px;background:var(--white)}

/* hero */
.hero{left:0;top:105px;width:1200px;height:540px;background:linear-gradient(90deg,#3ea85a 0%,#52b56a 45%,#8fb9a8 65%,#b9c9d6 100%)}
.hero-copy{color:var(--white)}

/* facilities */
.band{left:0;width:1200px;background:var(--green)}
.fac-card{position:absolute;top:869px;width:325px;height:465px;background:var(--white);box-shadow:0 4px 14px rgba(0,0,0,.06)}
.fac-card .img{position:absolute;left:0;top:0;width:325px;height:259px}
.fac-card .icon{position:absolute;left:26px;top:193px;width:67px;height:67px;background:var(--green);display:flex;align-items:center;justify-content:center}
.fac-card h3{position:absolute;left:25px;top:288px;font-size:21px;font-weight:400}
.fac-card p{position:absolute;left:25px;top:326px;width:250px;font-size:13px;line-height:17px;color:var(--text);font-weight:300}
.fac-card .more{left:25px;top:414px}

/* about */
.feature h4{font-size:21px;font-weight:400;margin-top:10px}
.feature p{font-size:13px;line-height:21px;color:var(--text);font-weight:300;margin-top:12px;width:260px}

/* services */
.svc{position:absolute;top:2195px;width:236px;height:333px;background:var(--white);box-shadow:0 4px 14px rgba(0,0,0,.05)}
.svc .img{position:absolute;left:13px;top:14px;width:210px;height:156px}
.svc h3{position:absolute;left:23px;top:186px;font-size:21px;font-weight:400}
.svc p{position:absolute;left:23px;top:226px;width:185px;font-size:13px;line-height:17px;color:var(--text);font-weight:300}
.svc .more{left:23px;top:293px}

/* form */
.field{position:absolute;background:var(--field);font-size:15px;color:#888;padding:0 22px;display:flex;align-items:center}

/* footer */
.footer{left:0;top:3550px;width:1200px;height:405px;background:var(--footer);color:var(--white)}
.fcol{position:absolute;top:85px}
.fcol h5{font-size:23px;font-weight:400;margin-bottom:25px}
.fcol li{list-style:none;font-size:13px;font-weight:300;height:34px}
.fsocial{position:absolute;top:238px;width:43px;height:43px;background:#4a4b4d;display:flex;align-items:center;justify-content:center}
</style>
</head>
<body>

<!-- header -->
<div class="abs logo-box">
  <div class="mark"></div>
  <div class="name">maple grove</div>
  <div class="sub">pediatric dentistry</div>
</div>
<div class="abs topbar">
  <div class="item" style="left:26px">
    <svg width="13" height="13" viewBox="0 0 24 24"><path fill="#fff" d="M6.6 10.8a15.1 15.1 0 0 0 6.6 6.6l2.2-2.2c.3-.3.7-.4 1-.2 1.1.4 2.3.6 3.6.6.6 0 1 .4 1 1V20c0 .6-.4 1-1 1A17 17 0 0 1 3 4c0-.6.4-1 1-1h3.5c.6 0 1 .4 1 1 0 1.3.2 2.5.6 3.6.1.3 0 .7-.2 1z"/></svg>
    +1800-555-0142
  </div>
  <div class="sep" style="left:168px"></div>
  <div class="item" style="left:190px">
    <svg width="15" height="12" viewBox="0 0 24 18"><path fill="#fff" d="M0 0h24v18H0z"/><path d="M1 1l11 8 11-8" stroke="#37a44f" stroke-width="2" fill="none"/></svg>
    hello@maplegrove-dental.com
  </div>
  <div class="sep" style="left:935px"></div>
  <div class="item" style="left:957px"><span class="social-dot" aria-label="Social link one"></span></div>
  <div class="sep" style="left:982px"></div>
  <div class="item" style="left:1002px"><span class="social-dot" aria-label="Social link two"></span></div>
</div>
<nav class="abs navrow">
  <a class="link" style="left:504px">Home</a>
  <a class="link" style="left:576px">Meet Our Dentists</a>
  <a class="link" style="left:725px">Services</a>
  <a class="link" style="left:812px">Contact Us</a>
  <div class="abs" style="left:908px;top:0;width:1px;height:57px;background:#e5e5e5"></div>
  <svg class="abs" style="left:928px;top:19px" width="19" height="19" viewBox="0 0 20 20"><circle cx="8" cy="8" r="6.5" stroke="#333" stroke-width="1.6" fill="none"/><path d="M13 13l6 6" stroke="#333" stroke-width="1.6"/></svg>
</nav>
<div class="abs menu-box"><span></span><span></span><span></span></div>

<!-- hero -->
<section class="abs hero">
  <div class="photo" role="img" aria-label="Dentist showing a model of teeth to a young girl in a dental chair" style="left:530px;top:0;width:670px;height:540px;background:linear-gradient(120deg,#7fae97,#a9c3cf 60%,#c9d3dc)"></div>
  <div class="hero-copy">
    <div class="badge" style="left:86px;top:122px;background:rgba(255,255,255,.28);color:var(--white)">Partnership for health</div>
    <h1 class="abs" style="left:83px;top:180px;font-size:44px;font-weight:400;line-height:56px;width:560px">Modern Dentistry with Unique Technologies</h1>
    <p class="abs" style="left:86px;top:303px;width:435px;font-size:13px;line-height:21px;font-weight:300">Lorem Ipsum is simply dummy text of the printing and typesetting industry. Lorem Ipsum has been the industry's standard dummy text ever since Athe 1500s</p>
    <div class="btn" style="left:86px;top:389px;width:127px;height:43px;background:rgba(255,255,255,.2)">Read More &nbsp;+</div>
  </div>
</section>

<!-- facilities -->
<section class="abs band" style="top:645px;height:483px"></section>
<div class="badge white" style="left:518px;top:734px">What we provide</div>
<h2 class="h2" style="left:0;width:1200px;text-align:center;top:785px;color:var(--white)">What Facilities We Provided</h2>

<div class="fac-card" style="left:86px">
  <div class="img" role="img" aria-label="Dentist showing an x-ray to a child and parent" style="background:linear-gradient(135deg,#7f97a6,#c7d2d9)"></div>
  <div class="icon"><svg width="30" height="32" viewBox="0 0 30 32" fill="none" stroke="#fff" stroke-width="1.6"><circle cx="15" cy="9" r="6"/><path d="M3 31c0-7 5-11 12-11s12 4 12 11z"/></svg></div>
  <h3>Pediatric orthodontics</h3>
  <p>There are many variations of pas of Lorem Ipsum available.There are many variations of pas of Lorem Ipsum available.</p>
  <span class="more">Read More &nbsp;+</span>
</div>
<div class="fac-card" style="left:437px">
  <div class="img" role="img" aria-label="Smiling boy in a dental chair giving a thumbs up" style="background:linear-gradient(135deg,#9fb6c2,#d6dfe4)"></div>
  <div class="icon"><svg width="30" height="32" viewBox="0 0 30 32" fill="none" stroke="#fff" stroke-width="1.6"><circle cx="15" cy="9" r="6"/><path d="M3 31c0-7 5-11 12-11s12 4 12 11z"/></svg></div>
  <h3>Two-phase treatment</h3>
  <p>There are many variations of pas of Lorem Ipsum available.There are many variations of pas of Lorem Ipsum available.</p>
  <span class="more">Read More &nbsp;+</span>
</div>
<div class="fac-card" style="left:787px">
  <div class="img" role="img" aria-label="Dentist holding a dental model with gloved hands" style="background:linear-gradient(135deg,#d7e2e6,#7fc7c9)"></div>
  <div class="icon"><svg width="30" height="32" viewBox="0 0 30 32" fill="none" stroke="#fff" stroke-width="1.6"><circle cx="15" cy="9" r="6"/><path d="M3 31c0-7 5-11 12-11s12 4 12 11z"/></svg></div>
  <h3>Orthodontic maintenance</h3>
  <p>There are many variations of pas of Lorem Ipsum available.There are many variations of pas of Lorem Ipsum available.</p>
  <span class="more">Read More &nbsp;+</span>
</div>

<!-- about -->
<div class="badge soft" style="left:86px;top:1422px">What about us</div>
<h2 class="h2" style="left:85px;top:1472px;width:500px;line-height:51px">We Provide the Best Dental Service</h2>
<p class="abs" style="left:86px;top:1594px;width:545px;font-size:13px;line-height:21px;color:var(--text);font-weight:300">Lorem Ipsum is simply dummy text of the printing and typesetting industry. Lorem Ipsum has been the industry's standard dummy text ever since the 1500s, when an unknown printer</p>
<div class="abs feature" style="left:86px;top:1682px">
  <svg width="42" height="34" viewBox="0 0 42 34" fill="none" stroke="#2f9a46" stroke-width="1.6"><path d="M4 6c4-5 9-3 12-1 3-2 8-4 12 1 3 5 0 12-2 18-1 4-4 4-5 0l-2-6-2 6c-1 4-4 4-5 0C10 18 1 11 4 6z"/><circle cx="31" cy="22" r="8"/><path d="M31 18v8M27 22h8"/></svg>
  <h4>Dental Prevention</h4>
  <p>Lorem Ipsum is simply dummy text of the printing</p>
</div>
<div class="abs feature" style="left:364px;top:1682px">
  <svg width="42" height="34" viewBox="0 0 42 34" fill="none" stroke="#2f9a46" stroke-width="1.6"><path d="M6 7c4-5 9-3 12-1 3-2 8-4 12 1 3 5 0 12-2 18-1 4-4 4-5 0l-2-6-2 6c-1 4-4 4-5 0C12 19 3 12 6 7z"/><path d="M30 3l6-2M33 8l6 0"/></svg>
  <h4>Dental Services</h4>
  <p>Lorem Ipsum is simply dummy text of the printing</p>
</div>
<div class="btn" style="left:86px;top:1845px;width:126px;height:42px">Read More &nbsp;+</div>
<div class="photo" role="img" aria-label="Boy sitting in a yellow dental chair" style="left:778px;top:1421px;width:335px;height:410px;background:linear-gradient(160deg,#e3b43c 0%,#cfd4d6 40%,#1f3550 85%)"></div>
<div class="photo" role="img" aria-label="Dentist examining a child's teeth" style="left:666px;top:1655px;width:207px;height:230px;background:linear-gradient(160deg,#c9b9a8,#3c3f45 60%,#9aa0a6);border:4px solid #fff;border-left:0;border-bottom:0"></div>

<!-- services -->
<section class="abs" style="left:0;top:1972px;width:1200px;height:645px;background:var(--light)"></section>
<div class="badge soft" style="left:526px;top:2061px">Our services</div>
<h2 class="h2" style="left:0;width:1200px;text-align:center;top:2113px">Explore Our Main Service</h2>
<div class="svc" style="left:86px">
  <div class="img" role="img" aria-label="Girl in an orange dental chair during a filling" style="background:linear-gradient(135deg,#e98a2c,#e5c07c 60%,#5f6b80)"></div>
  <h3>Dental Filling</h3>
  <p>There are many variations of pas of Lorem Ipsum available.</p>
  <span class="more">Read More &nbsp;+</span>
</div>
<div class="svc" style="left:351px">
  <div class="img" role="img" aria-label="Hands holding a tooth model showing the root" style="background:linear-gradient(135deg,#d8e6ee,#e39cb8 50%,#c9d9e3)"></div>
  <h3>Root Canal</h3>
  <p>There are many variations of pas of Lorem Ipsum available.</p>
  <span class="more">Read More &nbsp;+</span>
</div>
<div class="svc" style="left:612px">
  <div class="img" role="img" aria-label="Girl sitting in a blue dental chair" style="background:linear-gradient(135deg,#d9e3ea,#7ea2c4 55%,#e4e8ec)"></div>
  <h3>Dental Implant</h3>
  <p>There are many variations of pas of Lorem Ipsum available.</p>
  <span class="more">Read More &nbsp;+</span>
</div>
<div class="svc" style="left:878px">
  <div class="img" role="img" aria-label="Gloved hand holding a dental model with braces" style="background:linear-gradient(135deg,#dfe6ec,#e27a86 55%,#e9edf1)"></div>
  <h3>Braces &amp; Aligners</h3>
  <p>There are many variations of pas of Lorem Ipsum available.</p>
  <span class="more">Read More &nbsp;+</span>
</div>

<!-- call to action -->
<section class="abs band" style="top:2617px;height:233px"></section>
<h2 class="h2" style="left:85px;top:2686px;width:620px;color:var(--white);line-height:51px">A great place of medical hospital center &amp; dental care</h2>
<div class="btn" style="left:973px;top:2712px;width:141px;height:42px;background:var(--white);color:var(--green-dark)">Contact Us &nbsp;+</div>

<!-- appointment -->
<div class="photo" role="img" aria-label="Dentist in a mask with a smiling girl holding a toy" style="left:86px;top:2936px;width:439px;height:527px;background:linear-gradient(150deg,#e9e6e3,#c9c5c2 50%,#3a3a3c 90%)"></div>
<div class="badge soft" style="left:577px;top:2938px">Appointment</div>
<h2 class="h2" style="left:576px;top:2990px;width:500px;line-height:51px">Apply for free Dental Checkup</h2>
<div class="field" style="left:577px;top:3113px;width:261px;height:51px">Your Name</div>
<div class="field" style="left:853px;top:3113px;width:261px;height:51px">Gender</div>
<div class="field" style="left:577px;top:3185px;width:261px;height:51px">Your Email</div>
<div class="field" style="left:853px;top:3185px;width:261px;height:51px">Phone No.</div>
<div class="field" style="left:577px;top:3262px;width:537px;height:115px;align-items:flex-start;padding-top:20px">Your Message</div>
<div class="btn" style="left:574px;top:3405px;width:132px;height:43px">Send Message</div>

<!-- footer -->
<footer class="abs footer">
  <div class="abs" style="left:86px;top:73px;width:160px;text-align:center">
    <div style="width:34px;height:34px;border-radius:50%;background:var(--green);margin:0 auto 4px"></div>
    <div style="font-size:20px;line-height:1">maple grove</div>
    <div style="font-size:7px;letter-spacing:2px;text-transform:uppercase;margin-top:3px">pediatric dentistry</div>
  </div>
  <p class="abs" style="left:86px;top:162px;width:260px;font-size:13px;line-height:21px;font-weight:300">It helps designers plan out where the content will sit, the content to be written and approved.</p>
  <div class="fsocial" style="left:86px" aria-label="Social link one"><span class="social-dot"></span></div>
  <div class="fsocial" style="left:139px" aria-label="Social link two"><span class="social-dot"></span></div>
  <div class="fcol" style="left:437px"><h5>Main Menu</h5><ul><li>Home</li><li>About Us</li><li>Meet Our Dentists</li><li>Services</li><li>Contact</li></ul></div>
  <div class="fcol" style="left:646px"><h5>Quick Links</h5><ul><li>FAQ</li><li>Doctors</li><li>Departments</li><li>Events</li><li>Member</li></ul></div>
  <div class="fcol" style="left:855px;width:280px"><h5>Contact</h5><ul><li>Call : +1800-555-0142</li><li>Email : hello@maplegrove-dental.com</li><li style="line-height:20px;height:auto">Location : Lorem ipsum dolor sit amet, consectetur adipiscing elit.</li></ul></div>
  <div class="abs" style="left:0;top:334px;width:1200px;height:1px;background:rgba(255,255,255,.12)"></div>
  <p class="abs" style="left:0;top:354px;width:1200px;text-align:center;font-size:13px;font-weight:300">Copyright 2022 Maple Grove. All Rights Reserved</p>
</footer>

</body>
</html>
```